Bramwell Ridge Minerals

Looking for a cool, glossy business card...white with our logo on one side and then the a smaller version of the logo on the other side (top left hand corner) and then the name and position of the person next to it, and then the office address and email address on the bottom left hand corner and the phone numbers & email address on the bottom right hand corner. I have the logo already...can pass it on when you're ready.

```html
<!DOCTYPE html>
<html lang="en">
<head>
<meta charset="utf-8">
<title>Bramwell Ridge Minerals — Business Card</title>
<link rel="stylesheet" href="https://fonts.googleapis.com/css2?family=Cinzel:wght@400;600&family=Crimson+Text:wght@400&display=swap">
<style>
  :root {
    --backdrop: #1f1f21;
    --card: #ffffff;
    --ink: #2b2b30;
    --ink-soft: #45454c;
    --flag-blue: #2b3f9e;
    --flag-red: #c8202f;
    --rule: #9a9aa2;
  }
  * { box-sizing: border-box; margin: 0; padding: 0; }
  html, body {
    width: 1200px; height: 900px; overflow: hidden;
    background: var(--backdrop);
  }
  .sheet {
    width: 1200px; height: 900px;
    display: flex; flex-direction: column;
    align-items: center; justify-content: center;
    gap: 40px;
  }
  .card {
    position: relative;
    width: 700px; height: 400px;
    background: var(--card);
    box-shadow: 0 10px 30px rgba(0,0,0,.45);
  }

  /* wordmark */
  .wordmark {
    display: flex; align-items: center; gap: 12px;
    font-family: "Cinzel", serif;
    font-weight: 400;
    color: var(--ink);
    white-space: nowrap;
  }
  .wordmark__square {
    flex: none;
    background: var(--flag-blue);
  }

  /* logo side */
  .card--logo { display: flex; align-items: center; justify-content: center; }
  .card--logo .wordmark { font-size: 38px; letter-spacing: 1px; }
  .card--logo .wordmark__square { width: 16px; height: 16px; }

  /* details side */
  .card--details .wordmark {
    position: absolute; left: 40px; top: 48px;
    font-size: 22px; letter-spacing: .5px;
  }
  .card--details .wordmark__square { width: 10px; height: 10px; }

  .person {
    position: absolute; right: 48px; top: 170px;
    text-align: right; color: var(--ink);
  }
  .person__name {
    font-family: "Cinzel", serif; font-weight: 600;
    font-size: 24px; letter-spacing: 1px;
  }
  .person__role {
    font-family: "Cinzel", serif; font-weight: 400;
    font-size: 11px; letter-spacing: 5px; margin-top: 4px;
    color: var(--ink-soft);
  }

  .contact {
    position: absolute; bottom: 42px;
    display: flex; align-items: stretch; gap: 12px;
    font-family: "Crimson Text", serif;
    font-size: 15px; color: var(--ink);
    line-height: 24px;
  }
  .contact--office { left: 40px; }
  .contact--direct { right: 40px; text-align: right; }
  .contact__icons {
    display: flex; flex-direction: column; justify-content: space-around;
  }
  .contact__icons svg { width: 14px; height: 14px; display: block; }
  .contact__rule { width: 1px; background: var(--rule); }
</style>
</head>
<body>
<main class="sheet">

  <section class="card card--logo" aria-label="Card front">
    <div class="wordmark">
      <span class="wordmark__square"></span>
      <span class="wordmark__name">Bramwell Ridge Minerals</span>
    </div>
  </section>

  <section class="card card--details" aria-label="Card back">
    <div class="wordmark">
      <span class="wordmark__square"></span>
      <span class="wordmark__name">Bramwell Ridge Minerals</span>
    </div>

    <div class="person">
      <p class="person__name">Callum Hartley</p>
      <p class="person__role">MANAGING DIRECTOR</p>
    </div>

    <div class="contact contact--office">
      <div class="contact__icons">
        <svg viewBox="0 0 14 14" aria-hidden="true">
          <path d="M7 1a4 4 0 0 1 4 4c0 3-4 8-4 8S3 8 3 5a4 4 0 0 1 4-4z" fill="var(--flag-blue)"/>
          <circle cx="7" cy="5" r="1.5" fill="#fff"/>
        </svg>
        <svg viewBox="0 0 14 14" aria-hidden="true">
          <rect x="1" y="3" width="12" height="8" fill="var(--flag-red)"/>
          <path d="M1 3l6 5 6-5" fill="none" stroke="#fff" stroke-width="1.2"/>
        </svg>
      </div>
      <span class="contact__rule"></span>
      <div class="contact__lines">
        <p>218 Alder Creek Rd Suite B, Fenwick, OR 97411</p>
        <p>info@bramwellridgeminerals.com</p>
      </div>
    </div>

    <div class="contact contact--direct">
      <div class="contact__lines">
        <p>555-014-2286</p>
        <p>www.bramwellridgeminerals.com</p>
      </div>
      <span class="contact__rule"></span>
      <div class="contact__icons">
        <svg viewBox="0 0 14 14" aria-hidden="true">
          <path d="M4 1.5l2 2.5-1.2 1.4c.7 1.6 1.9 2.8 3.5 3.5L9.7 7.7l2.5 2-1.2 2.3C6 11.8 2.2 8 2 3z" fill="var(--flag-red)"/>
        </svg>
        <svg viewBox="0 0 14 14" aria-hidden="true">
          <circle cx="7" cy="7" r="5.5" fill="none" stroke="var(--flag-blue)" stroke-width="1.2"/>
          <ellipse cx="7" cy="7" rx="2.4" ry="5.5" fill="none" stroke="var(--flag-blue)" stroke-width="1"/>
          <path d="M1.5 7h11M2.5 4.2h9M2.5 9.8h9" stroke="var(--flag-blue)" stroke-width="1"/>
        </svg>
      </div>
    </div>
  </section>

</main>
</body>
</html>
```